Need Web Page Created

Our company is need to have 3 web pages created (home page, about, contact) using basic html (css is ok). Not looking to use flash or swf, but something that could be used on all browsers and platforms.

I've attached an example design as what we are looking for (as well as logo). The orangish color that is in the logo design should be used on web pages where shown.

Looking for a nice smooth transition between page to page and the page icons up at the top right hand corner should change color based on the page you are viewing (color change can be white or the orangish color from logo).

It Company

```html
<!DOCTYPE html>
<html lang="en">
<head>
<meta charset="utf-8">
<title>Lumen Forge Works</title>
<link rel="stylesheet" href="https://fonts.googleapis.com/css2?family=Open+Sans:wght@300;400;700&display=swap">
<style>
  :root {
    --orange: #d6802a;
    --gear-orange: #bc8649;
    --gear-grey: #939393;
    --charcoal: #4a4a4c;
    --ink: #555555;
    --page: #e1e1e1;
    --bar: #2e2e30;
    --white: #ffffff;
  }
  * { box-sizing: border-box; margin: 0; padding: 0; }
  html, body { width: 1200px; height: 782px; overflow: hidden; }
  body {
    position: relative;
    background: var(--page);
    font-family: "Open Sans", Arial, sans-serif;
    color: var(--ink);
  }
  .top-bar {
    position: absolute; left: 0; top: 0; width: 1200px; height: 13px;
    background: var(--bar); border-bottom: 4px solid var(--orange);
  }
  .gear-art {
    position: absolute; left: 0; top: 0; width: 1200px; height: 782px;
  }
  .brand {
    position: absolute; left: 0; width: 1200px; top: 66px;
    display: flex; justify-content: center; align-items: center; gap: 12px;
  }
  .brand-dot {
    width: 22px; height: 22px; border-radius: 50%; background: var(--orange);
  }
  .brand-name {
    font-size: 32px; font-weight: 400; color: var(--charcoal);
    text-transform: uppercase; letter-spacing: 0.5px;
  }
  .page-nav {
    position: absolute; top: 35px; right: 79px; display: flex; gap: 8px;
  }
  .page-nav a {
    width: 37px; height: 37px; border-radius: 50%;
    background: var(--charcoal); display: flex; align-items: center; justify-content: center;
  }
  .page-nav a.is-current { background: var(--orange); }
  .headline {
    position: absolute; right: 78px; top: 262px; text-align: right;
    text-transform: uppercase; white-space: nowrap;
  }
  .headline-light {
    display: block; font-weight: 300; font-size: 66px; line-height: 66px;
    color: var(--ink); letter-spacing: -0.5px;
  }
  .headline-strong {
    display: block; font-size: 44px; line-height: 54px; font-weight: 700; color: var(--ink);
  }
  .headline-strong .accent { font-weight: 400; color: var(--orange); }
  .quote {
    position: absolute; right: 78px; top: 572px; width: 330px;
    text-align: right; font-size: 14px; line-height: 17px; color: var(--ink);
  }
  .quote cite { font-style: normal; font-weight: 700; color: var(--orange); }
  .site-footer {
    position: absolute; left: 0; top: 726px; width: 1200px; height: 56px;
    background: rgba(40, 40, 42, 0.93); border-top: 5px solid var(--orange);
    display: flex; align-items: center; justify-content: space-between;
    padding: 0 78px; color: var(--white); font-size: 14px;
  }
  .footer-contact { display: flex; align-items: center; gap: 14px; }
  .footer-dot {
    width: 26px; height: 26px; border-radius: 50%; border: 2px solid var(--white);
  }
</style>
</head>
<body>
  <div class="top-bar"></div>

  <svg class="gear-art" role="img" aria-label="Decorative gear illustration: a large orange gear on the left and a grey gear rising from the footer" viewBox="0 0 1200 782">
    <circle cx="116" cy="504" r="320" fill="var(--gear-orange)"/>
    <circle cx="566" cy="790" r="200" fill="var(--gear-grey)"/>
  </svg>

  <header class="brand">
    <span class="brand-dot"></span>
    <span class="brand-name">Lumen Forge Works</span>
  </header>

  <nav class="page-nav" aria-label="Pages">
    <a class="is-current" href="#home" aria-label="Home">
      <svg width="20" height="18" viewBox="0 0 20 18"><path d="M10 1 L19 9 H16 V17 H4 V9 H1 Z" fill="#3a3a3a"/></svg>
    </a>
    <a href="#about" aria-label="About">
      <svg width="12" height="22" viewBox="0 0 12 22"><circle cx="6" cy="3.5" r="3" fill="#d6802a"/><path d="M2 9 H8 V19 H10 V21 H2 V19 H4 V11 H2 Z" fill="#d6802a"/></svg>
    </a>
    <a href="#contact" aria-label="Contact">
      <svg width="22" height="15" viewBox="0 0 22 15"><rect x="0.5" y="0.5" width="21" height="14" fill="#d6802a"/><path d="M1 1 L11 9 L21 1" fill="none" stroke="#4a4a4c" stroke-width="1.6"/></svg>
    </a>
  </nav>

  <h1 class="headline">
    <span class="headline-light">Today’s Idea For</span>
    <span class="headline-strong">Tomorrow’s <span class="accent">Technology</span></span>
  </h1>

  <blockquote class="quote">
    "One's mind, once stretched by a new idea, never regains its original dimensions." - <cite>Marguerite Ashdown</cite>
  </blockquote>

  <footer class="site-footer">
    <span class="copyright">© 2014 Lumen Forge Works</span>
    <span class="footer-contact"><span class="footer-dot"></span>Phone (USA): 1-555-010-4477</span>
  </footer>
</body>
</html>
```